New Web Page Design - Cement Rendering Business

Looking for a overhaul of our existing website (www.norpex.com.au).

Looking for a sleek and elegant design that incorporates the colours of our logos, black / green and white. Needs to look professional and want it to be well above what our competition is offering. (Findora search for 'cement rendering sydney' will display the competition we want to be well ahead of.

Prefer a mixture of pages with black background and white alternatively between home (black), about us (white), contact us (black) and gallery (white).

Would like to incorporate our logo on all pages attached preferably in the top left corner.

Website needs to be search engine optimised and have easily updated photo gallery which we already have.

Also need to embed our trackwise metrics code on the front home page.

Website needs to be able easily updated (text, pictures ) as required.
content management system should include fields where you can alter your page titles, meta description and keywords.

Pages also needs to be optimised for mobile devices, iphone, ipad and other mobile devices. (it is a current feature we have)

If you have any questions, just message me.

Please remember the look and feel of the site is important to us, we don't want it over complicated, simple elegant and professional in line with our logo standards.
Updates

Hi All, As an example of the look and feel we like. We have found a site that may assist in your design and creative process. http://demo.quorvix.org/ We like the simplicity, elegance and professional look of this site, although we would like it with our images, colours and logos. I hope this helps.! keep the great designs coming!

All, Thanks for the designs. Please try and use our website images due to copyright reasons for all your designs. Tomas

Target Market(s)

Construction Companies

Industry/Entity Type

Business

Colors
9bcb3b
acd036
474747

Requirements
Must have
• Search Engine Optimised.
Photo Gallery
Elegant/Professional Look & Feel.
Simple Yet Effective
Nice to have
• Moving Parts
Should not have
• Overly Complicated.
Cheap & Traditional Looking.
Boring

```html
<!DOCTYPE html>
<html lang="en">
<head>
<meta charset="utf-8">
<title>Norpex Cement Rendering</title>
<link rel="stylesheet" href="https://fonts.googleapis.com/css2?family=Open+Sans:wght@400;600;700&display=swap">
<style>
:root{
  --green:#9bcb3b;
  --green-2:#acd036;
  --charcoal:#474747;
  --charcoal-dark:#3b3b3b;
  --footer:#3d3d3d;
  --ink:#222;
  --white:#fff;
  --paper:#e6e6e6;
  --orange:#f26a21;
  --maroon:#a0122f;
  --muted:#cfcfcf;
}
*{box-sizing:border-box;margin:0;padding:0}
html,body{width:1200px;height:2748px;overflow:hidden}
body{position:relative;background:var(--charcoal);font-family:"Open Sans",Arial,sans-serif;color:var(--white)}
.abs{position:absolute}

/* hero */
.hero{left:0;top:0;width:1200px;height:620px;background:linear-gradient(160deg,#8a9aa8 0%,#a9b3b6 30%,#7d7f78 55%,#5e5b55 100%)}
.hero-accent{left:700px;top:0;width:500px;height:560px;background:radial-gradient(ellipse at 60% 45%,rgba(250,215,40,.85) 0 18%,rgba(70,100,150,.55) 34%,rgba(0,0,0,0) 62%)}
.topbar{left:0;top:0;width:1200px;height:80px;background:rgba(40,40,40,.55)}
.brand{left:97px;top:0;width:201px;height:160px;background:rgba(60,60,60,.92);display:flex;flex-direction:column;align-items:center;justify-content:center;gap:8px}
.brand-mark{width:46px;height:46px;border-radius:50%;background:var(--green)}
.brand-name{font-size:30px;font-weight:600;color:var(--green);letter-spacing:2px;line-height:1}
.brand-tag{font-size:11px;color:var(--green);line-height:1}
.nav{left:588px;top:0;height:80px;display:flex}
.nav a{display:flex;align-items:center;height:80px;padding:0 18px;font-size:14px;color:var(--white);text-decoration:none;text-transform:uppercase}
.nav a.active{background:var(--green)}
.slide-arrow{top:335px;width:60px;height:62px;background:rgba(30,30,30,.75);display:flex;align-items:center;justify-content:center}

/* feature cards */
.card{top:612px;width:318px;height:348px;background:var(--white);border-top:8px solid var(--green);box-shadow:0 4px 10px rgba(0,0,0,.4);color:var(--ink);text-align:center}
.card-icon{position:absolute;left:64px;top:-86px;width:190px;height:190px;border-radius:50%;background:var(--white);border:6px solid #d9d9d9;display:flex;align-items:center;justify-content:center}
.card h2{position:absolute;top:130px;width:100%;font-size:23px;font-weight:700;letter-spacing:1px}
.card p{position:absolute;top:180px;left:22px;right:22px;font-size:11.5px;line-height:1.45}
.card .btn{position:absolute;left:98px;top:276px;width:120px;height:40px;border:2px solid var(--ink);font-size:14px;font-weight:600;display:flex;align-items:center;justify-content:center}
.card .btn.filled{background:var(--green);border-color:var(--green);color:var(--white)}

/* newsletter */
.newsletter{left:97px;top:1020px;width:1003px;height:145px;background:var(--green);display:flex;align-items:center;padding:0 14px}
.newsletter h3{font-size:29px;font-weight:400;margin-left:14px;width:330px}
.newsletter p{font-size:13px;line-height:1.35;width:260px;margin-left:26px}
.newsletter .field{margin-left:22px;width:220px;height:32px;background:var(--white);color:#999;font-size:13px;padding:6px 10px}
.newsletter .submit{width:92px;height:32px;background:var(--ink);font-size:14px;display:flex;align-items:center;justify-content:center}

/* about band */
.about{left:0;top:1188px;width:1200px;height:374px;background:var(--paper);color:var(--ink)}
.about-photo{left:100px;top:27px;width:435px;height:320px;background:linear-gradient(180deg,#5e87b8 0%,#9db1c4 35%,#e9ecee 55%,#8f8a80 80%,#5d5a52 100%)}
.about h2{left:565px;top:34px;font-size:34px;font-weight:600;color:var(--orange);letter-spacing:1px}
.about h3{left:565px;top:84px;font-size:25px;font-weight:400;line-height:1.25;color:#444;width:500px;text-transform:uppercase}
.about p{left:565px;top:152px;width:525px;font-size:12px;line-height:1.4}
.checks{left:565px;top:222px;list-style:none}
.checks li{display:flex;align-items:center;gap:10px;font-size:11.5px;font-weight:700;height:28px;text-transform:uppercase}
.about .cta{left:920px;top:304px;width:168px;height:44px;border-radius:10px;background:var(--maroon);color:var(--white);font-size:15px;display:flex;align-items:center;justify-content:center}

/* projects */
.section-title{left:97px;top:1612px;width:1003px;height:50px;display:flex;align-items:center;gap:20px}
.section-title .rule{flex:1;height:1px;background:#9a9a9a}
.section-title h2{font-size:34px;font-weight:700;letter-spacing:1px}
.section-title h2 span{color:var(--green)}
.thumb{top:1695px;width:223px;height:225px;border:3px solid var(--white)}
.thumb.active{display:flex;flex-direction:column;align-items:center;justify-content:center;gap:10px}
.thumb .overlay{position:absolute;inset:0;background:rgba(155,203,59,.82)}
.thumb .plus,.thumb .label{position:relative}
.thumb .label{font-size:30px}
.pager{top:1944px;width:44px;height:44px;border:2px solid var(--white);display:flex;align-items:center;justify-content:center}
.pager.next{border-color:var(--green)}

/* posts */
.post{top:2075px;width:488px;height:215px;border:2px solid #d6d6d6;display:flex}
.post-img{width:200px;height:100%}
.post-body{padding:12px 18px}
.post h3{font-size:21px;font-weight:400;line-height:1.25;text-transform:uppercase}
.post p{font-size:12px;line-height:1.35;margin-top:18px}

/* footer */
.footer{left:0;top:2355px;width:1200px;height:393px;background:var(--footer);border-top:9px solid var(--green)}
.footer h4{position:absolute;font-size:17px;font-weight:400;color:var(--green);text-transform:uppercase}
.social{position:absolute;left:107px;top:98px;display:flex;gap:14px}
.social span{width:36px;height:36px;border-radius:50%;background:var(--green)}
.blog{position:absolute;left:107px;top:198px;width:280px;font-size:12px;line-height:1.4}
.blog strong{font-size:14px;display:block}
.blog .date{color:var(--green);font-size:10px}
.blog .more{color:var(--green)}
.ad-list{position:absolute;left:447px;top:72px;width:275px;list-style:none}
.ad-list li{font-size:10.5px;font-weight:600;height:24px;border-bottom:1px solid #aaa;padding:4px 0 0 8px}
.input{position:absolute;left:818px;width:276px;background:#ede6e6;color:#888;font-size:12px;padding:6px 8px}
.send{position:absolute;left:818px;top:2635px;width:72px;height:28px;background:var(--green);font-size:11px;font-weight:700;display:flex;align-items:center;justify-content:center}
.legal{left:0;top:2700px;width:1200px;height:48px;background:var(--charcoal-dark);border-top:1px solid #5a5a5a;padding:0 107px;display:flex;align-items:center;font-size:11px;color:var(--green)}
</style>
</head>
<body>

<header>
  <div class="abs hero" role="img" aria-label="Photo of a builder holding a yellow hard hat and plans in front of scaffolding"></div>
  <div class="abs hero-accent"></div>
  <div class="abs topbar"></div>
  <div class="abs brand">
    <span class="brand-mark"></span>
    <span class="brand-name">NORPEX</span>
    <span class="brand-tag">Cement Rendering</span>
  </div>
  <nav class="abs nav">
    <a class="active">Home</a><a>About Us</a><a>Project</a><a>Quality Control</a><a>Contact Us</a>
  </nav>
  <div class="abs slide-arrow" style="left:0"><svg width="18" height="24"><path d="M14 2 4 12l10 10" fill="none" stroke="#fff" stroke-width="3"/></svg></div>
  <div class="abs slide-arrow" style="left:1140px"><svg width="18" height="24"><path d="M4 2l10 10L4 22" fill="none" stroke="#fff" stroke-width="3"/></svg></div>
</header>

<section>
  <article class="abs card" style="left:97px">
    <div class="card-icon">
      <svg width="100" height="90" viewBox="0 0 100 90">
        <circle cx="38" cy="52" r="22" fill="none" stroke="#9bcb3b" stroke-width="12" stroke-dasharray="7 5"/>
        <circle cx="38" cy="52" r="14" fill="#9bcb3b"/><circle cx="38" cy="52" r="6" fill="#fff"/>
        <circle cx="72" cy="26" r="14" fill="none" stroke="#9bcb3b" stroke-width="9" stroke-dasharray="5 4"/>
        <circle cx="72" cy="26" r="9" fill="#9bcb3b"/><circle cx="72" cy="26" r="4" fill="#fff"/>
      </svg>
    </div>
    <h2>TECHNOLOGY</h2>
    <p>Phasellus porta. Fusce suscipit varius mi. Cum sociis natoque penatibus et magnis dis parturient montes, nascetur ridiculus mus. Nulla dui. Fusce feugiat malesuada odio. Morbi nunc odio, gravida.</p>
    <div class="btn filled">MORE</div>
  </article>
  <article class="abs card" style="left:440px">
    <div class="card-icon">
      <svg width="80" height="96" viewBox="0 0 80 96">
        <rect x="8" y="4" width="60" height="78" fill="#fff" stroke="#333" stroke-width="3"/>
        <path d="M18 18h40M18 28h40M18 38h30" stroke="#333" stroke-width="3"/>
        <circle cx="50" cy="62" r="11" fill="#333"/>
        <path d="M44 70l-4 20 10-6 10 6-4-20" fill="#333"/>
      </svg>
    </div>
    <h2 style="font-size:21px">QUALITY CONTROL</h2>
    <p>Phasellus porta. Fusce suscipit varius mi. Cum sociis natoque penatibus et magnis dis parturient montes, nascetur ridiculus mus. Nulla dui. Fusce feugiat malesuada odio. Morbi nunc odio, gravida.</p>
    <div class="btn">MORE</div>
  </article>
  <article class="abs card" style="left:783px">
    <div class="card-icon">
      <div role="img" aria-label="Icon of construction staff in hard hats" style="width:96px;height:80px;border-radius:40px 40px 8px 8px;background:#333"></div>
    </div>
    <h2 style="top:142px;font-size:21px">THE STAFF</h2>
    <p>Phasellus porta. Fusce suscipit varius mi. Cum sociis natoque penatibus et magnis dis parturient montes, nascetur ridiculus mus. Nulla dui. Fusce feugiat malesuada odio. Morbi nunc odio, gravida.</p>
    <div class="btn">MORE</div>
  </article>
</section>

<section class="abs newsletter">
  <svg width="46" height="40" viewBox="0 0 46 40"><path d="M2 20 44 2 34 38 22 26 44 2 14 24z" fill="none" stroke="#fff" stroke-width="2.5" stroke-linejoin="round"/></svg>
  <h3>Subscribe To Newsletter</h3>
  <p>Lorem ipsum dolor sit amet, consectetur adipiscing elit, sed do eiusmod tempor incididunt ut labore</p>
  <div class="field">Email</div>
  <div class="submit">Submit</div>
</section>

<section class="abs about">
  <div class="abs about-photo" role="img" aria-label="Photo of a white company van parked at a building site"></div>
  <h2 class="abs">THE LEADING COMPANY</h2>
  <h3 class="abs">In the world of international trading</h3>
  <p class="abs">Lorem ipsum dolor sit amet, consectetuer adipiscing elit. Praesent vestibulum molestie lacus. Aenean nonummy hendrerit mauris. Phasellus porta. Fusce suscipit varius mi. Cum sociis natoque penatibus et magnis dis parturient montes.</p>
  <ul class="abs checks">
    <li><svg width="16" height="16"><rect x="1" y="1" width="14" height="14" fill="none" stroke="#222" stroke-width="1.5"/><path d="M3 8l4 4 8-10" fill="none" stroke="#222" stroke-width="2"/></svg>Sed in lacus ut enim adipiscing aliquet</li>
    <li><svg width="16" height="16"><rect x="1" y="1" width="14" height="14" fill="none" stroke="#222" stroke-width="1.5"/><path d="M3 8l4 4 8-10" fill="none" stroke="#222" stroke-width="2"/></svg>Sed in lacus ut enim adipiscing aliquet</li>
    <li><svg width="16" height="16"><rect x="1" y="1" width="14" height="14" fill="none" stroke="#222" stroke-width="1.5"/><path d="M3 8l4 4 8-10" fill="none" stroke="#222" stroke-width="2"/></svg>Sed in lacus ut enim adipiscing aliquet</li>
    <li><svg width="16" height="16"><rect x="1" y="1" width="14" height="14" fill="none" stroke="#222" stroke-width="1.5"/><path d="M3 8l4 4 8-10" fill="none" stroke="#222" stroke-width="2"/></svg>Sed in lacus ut enim adipiscing aliquet</li>
  </ul>
  <div class="abs cta">View Flash Intro</div>
</section>

<section>
  <div class="abs section-title"><span class="rule"></span><h2>OUR <span>PROJECT</span></h2><span class="rule"></span></div>
  <div class="abs thumb" style="left:97px;background:linear-gradient(135deg,#e3732f 0%,#b9b4ab 45%,#8d8a84 100%)" role="img" aria-label="Photo of a worker trowelling render"></div>
  <div class="abs thumb" style="left:357px;background:linear-gradient(180deg,#2f6db5 0%,#6f8db0 35%,#c7b7a0 60%,#6a5a48 100%)" role="img" aria-label="Photo of a rendered house under construction"></div>
  <div class="abs thumb active" style="left:617px;background:linear-gradient(135deg,#c26b3a,#9e9a92)" role="img" aria-label="Photo of a worker applying render">
    <span class="overlay"></span>
    <svg class="plus" width="36" height="36"><path d="M18 4v28M4 18h28" stroke="#fff" stroke-width="7"/></svg>
    <span class="label">Project 3</span>
  </div>
  <div class="abs thumb" style="left:877px;background:linear-gradient(135deg,#9b9790 0%,#c9c5bd 50%,#e06a2d 100%)" role="img" aria-label="Photo of render being spread with a trowel"></div>
  <div class="abs pager" style="left:548px"><svg width="12" height="18"><path d="M10 2 3 9l7 7" fill="none" stroke="#fff" stroke-width="3"/></svg></div>
  <div class="abs pager next" style="left:608px"><svg width="12" height="18"><path d="M2 2l7 7-7 7" fill="none" stroke="#9bcb3b" stroke-width="3"/></svg></div>
</section>

<section>
  <article class="abs post" style="left:97px">
    <div class="post-img" role="img" aria-label="Illustration of a yellow hard hat and drawing tools" style="background:linear-gradient(135deg,#f2c21a 0%,#c99a2a 45%,#8a7c60 100%)"></div>
    <div class="post-body">
      <h3 style="color:var(--green)">Perfect way to construct your home designs</h3>
      <p>Lorem ipsum dolor sit amet, consectetuer adipiscing elit. Praesent vestibulum molestie lacus. Aenean nonummy hendrerit mauris. Phasellus porta. Fusce . . . .</p>
    </div>
  </article>
  <article class="abs post" style="left:615px">
    <div class="post-img" role="img" aria-label="Photo of a freshly rendered wall" style="background:linear-gradient(90deg,#8e8a84 0%,#d8d4cc 50%,#9b968e 100%)"></div>
    <div class="post-body">
      <h3>How to choose the best cement</h3>
      <p style="margin-top:34px">Lorem ipsum dolor sit amet, consectetuer adipiscing elit. Praesent vestibulum molestie lacus. Aenean nonummy hendrerit mauris. Phasellus porta. Fusce . . . .</p>
    </div>
  </article>
</section>

<footer class="abs footer">
  <h4 style="left:107px;top:38px">Social Links</h4>
  <div class="social"><span></span><span></span><span></span></div>
  <h4 style="left:107px;top:162px">Blogs</h4>
  <div class="blog">
    <strong>Post Title</strong>
    <span class="date">Friday 8th April 2014</span><br>
    Lorem ipsum dolor sit amet, consectetur adipiscing elit. Nunc non diam erat. In fringilla massa ut nisi ullamcorper pellentesque.<br>
    <span class="more">Read More »</span>
  </div>
  <h4 style="left:447px;top:38px">Advertise With Us</h4>
  <ul class="ad-list">
    <li>Lorem ipsum dolor sit</li><li>Amet consectetur</li><li>Praesent vel sem id</li><li>Curabitur hendrerit est</li><li>Aliquam eget erat nec sapien</li><li>Cras id augue nunc</li><li>In nec justo non</li><li>Vivamus mollis enim ut</li><li>Curabitur hendrerit est</li>
  </ul>
  <h4 style="left:818px;top:38px">Contact Us</h4>
</footer>
<div class="input" style="top:2435px;height:30px">Name</div>
<div class="input" style="top:2475px;height:30px">Email</div>
<div class="input" style="top:2513px;height:112px">Message</div>
<div class="send">SUBMIT</div>
<div class="abs legal">Copyright © 2014 · All Rights Reserved</div>

</body>
</html>
```